Postcard Design

We are a licensed and insured remodeling contractor in Johnson County, KS. I am looking to get a professional look for our postcard advertising. I would prefer something that appeals to women, but is still masculine enough for a contractor. Here is the verbiage I would like in the postcard.
Ever question the references you get from a contractor? Wouldn't you prefer to get a reference from your neighbor?
We are currently working with one of your neighbors and would love the opportunity to work for you. You can look us up on our website and see some of the wonderful spaces we have helped create. Call us today to schedule an appointment and let us know how we can help you create the new space you have always dreamed of.
Tel: 555-302-1186
Fax:555-317-2094
WWW.BELTRIDGEHOMEWORKS.EXAMPLE
BELTRIDGEHOMEWORKS@MAILBOXLY.EXAMPLE
Here is the verbiage I would like to use.
We are working in your neighborhood.
Tel: 555-302-1186
Fax:555-317-2094

```html
<!DOCTYPE html>
<html lang="en">
<head>
<meta charset="utf-8">
<title>Beltridge Home Works – Neighborhood Postcard</title>
<link href="https://fonts.googleapis.com/css2?family=EB+Garamond:wght@400;700&display=swap" rel="stylesheet">
<style>
  :root {
    --teal: #68a5b0;
    --teal-text: #6e9fa8;
    --orange: #f47c12;
    --navy: #0c1a26;
    --mist: #e8f0f1;
    --paper: #ffffff;
    --cream: #fbf7ee;
  }
  * { margin: 0; padding: 0; box-sizing: border-box; }
  html, body {
    width: 1200px;
    height: 1000px;
    overflow: hidden;
    background: var(--paper);
  }
  .postcard {
    position: relative;
    width: 1200px;
    height: 1000px;
    font-family: "EB Garamond", Garamond, Georgia, serif;
    background:
      radial-gradient(ellipse 780px 700px at 120px 180px, var(--mist) 0%, rgba(232,240,241,0.85) 45%, rgba(255,255,255,0) 100%),
      var(--paper);
  }
  .copy {
    position: absolute;
    left: 79px;
    top: 66px;
    width: 590px;
  }
  .headline {
    color: var(--teal-text);
    font-weight: 700;
    font-size: 26.5px;
    line-height: 33px;
  }
  .body-text {
    margin-top: 40px;
    color: var(--teal-text);
    font-weight: 400;
    font-size: 26px;
    line-height: 33px;
  }
  .call-to-action {
    margin-top: 40px;
    color: var(--orange);
    font-weight: 700;
    font-size: 26.5px;
    line-height: 33px;
  }
  .divider {
    position: absolute;
    top: 565px;
    height: 15px;
  }
  .divider--teal { left: 0; width: 160px; background: var(--teal); }
  .divider--orange { left: 162px; width: 196px; background: var(--orange); }
  .divider--navy { left: 361px; width: 260px; background: var(--navy); }
  .contact-panel {
    position: absolute;
    left: 0;
    top: 589px;
    width: 622px;
    height: 236px;
    background: var(--teal);
    padding: 35px 0 0 79px;
  }
  .contact-panel p {
    color: var(--cream);
    font-weight: 700;
    font-size: 27px;
    line-height: 42px;
  }
</style>
</head>
<body>
  <div class="postcard">
    <div class="copy">
      <p class="headline">Ever question the references you get from a contractor?&nbsp; Wouldn’t you prefer to get a reference from your neighbor?</p>
      <p class="body-text">We are currently working with one of your neighbors and would love the opportunity to work for you. You can look us up on our website and see some of the wonderful spaces we have helped create.</p>
      <p class="call-to-action">Call us today to schedule an appointment and let us know how we can help you create the new space you have always dreamed of.</p>
    </div>

    <div class="divider divider--teal"></div>
    <div class="divider divider--orange"></div>
    <div class="divider divider--navy"></div>

    <div class="contact-panel">
      <p>Tel: (555) 302-1186</p>
      <p>Fax: (555) 317-2094</p>
      <p>beltridgehomeworks@mailboxly.example</p>
      <p>www.beltridgehomeworks.example</p>
    </div>
  </div>
</body>
</html>
```